Candidate Table Page

Need our intranet page redesigned. The layout is perfect and doesn't need to change. But the whole page doesn't seem to fit well together. Please change the font, feel, and table borders to make a more professional and easy user interface. symbols and/or icons are okay.

Target Market(s)

company staff

Industry/Entity Type

Security Guard

Coding

Coded - Design and coding required

Number of Pages Required

1 page

Font styles to use
Sans Serif

Colors
0255a3
fece3e

Requirements
Must have
• the employee information and columns
Nice to have
• icons and maybe symbols.

```html
<!DOCTYPE html>
<html lang="en">
<head>
<meta charset="utf-8">
<title>Candidates · Harborline Patrol Group</title>
<link rel="stylesheet" href="https://fonts.googleapis.com/css2?family=Source+Sans+3:wght@400;600;700&display=swap">
<style>
:root{
  --brand:#0255a3;
  --brand-deep:#013f7a;
  --brand-soft:#e8f0f9;
  --gold:#fece3e;
  --gold-soft:#fff4cf;
  --side:#1d2430;
  --side-line:#2a3240;
  --side-text:#c9d0db;
  --page:#eef1f5;
  --text:#27303d;
  --muted:#6b7584;
  --line:#e3e7ed;
  --row-alt:#f8f9fb;
  --ok:#1f8a4c;
  --ok-soft:#e4f4ea;
  --wait:#9a6a00;
  --plan:#0255a3;
}
*{box-sizing:border-box;margin:0;padding:0}
html,body{width:1200px;height:810px;overflow:hidden}
body{font-family:"Source Sans 3",Arial,sans-serif;color:var(--text);background:var(--page);position:relative}

.topbar{position:absolute;left:0;top:0;width:1200px;height:77px;background:#fff;border-bottom:3px solid var(--gold);z-index:2;display:flex;align-items:center;font-size:11px}
.brand{display:flex;align-items:center;gap:10px;margin-left:18px;width:232px}
.brand-mark{width:34px;height:34px;border-radius:50%;background:var(--gold);flex:none}
.brand-name{font-weight:700;font-size:15px;line-height:16px;color:var(--brand);width:130px;text-transform:uppercase;letter-spacing:.3px}
.filters{display:flex;align-items:center;gap:7px}
.label{font-size:10px;font-weight:600;color:var(--muted);text-transform:uppercase;letter-spacing:.5px}
.select{height:24px;border:1px solid #cfd6e0;border-radius:4px;background:#fff;font-size:10.5px;padding:0 8px;display:flex;align-items:center;justify-content:space-between;color:var(--text)}
.select span{color:var(--muted);font-size:8px}
.input{height:24px;width:98px;border:1px solid #cfd6e0;border-radius:4px;background:#fff}
.btn{height:24px;padding:0 14px;border-radius:4px;background:var(--brand);color:#fff;font-weight:600;font-size:11.5px;display:flex;align-items:center}
.btn.ghost{background:#fff;color:var(--brand);border:1px solid var(--brand)}
.user{position:absolute;right:20px;display:flex;align-items:center;gap:10px;font-size:12.5px;font-weight:600;color:var(--text)}

.sidebar{position:absolute;left:0;top:77px;width:198px;height:642px;background:var(--side)}
.nav-item{height:38px;display:flex;align-items:center;color:var(--side-text);font-size:12.5px;border-bottom:1px solid var(--side-line);border-left:3px solid transparent}
.nav-item .ico{width:40px;display:flex;justify-content:center}
.nav-item span{padding-left:8px}
.nav-item.active{background:var(--brand);color:#fff;border-left-color:var(--gold);font-weight:600}
.nav-item svg *{fill:var(--side-text)}
.nav-item svg .s{fill:none;stroke:var(--side-text)}
.nav-item.active svg *{fill:#fff}

.panel{position:absolute;left:220px;top:105px;width:962px;background:#fff;border:1px solid var(--line);border-radius:6px;overflow:hidden;box-shadow:0 1px 3px rgba(16,35,60,.06)}
table{border-collapse:collapse;width:962px;table-layout:fixed;font-size:10px}
th{background:var(--brand);color:#fff;font-weight:600;height:38px;text-align:left;padding-left:13px;font-size:10px;text-transform:uppercase;letter-spacing:.3px;border-bottom:3px solid var(--gold);white-space:nowrap}
th.tight{padding-left:5px;font-size:9px;letter-spacing:0}
td{height:31.3px;padding-left:13px;border-bottom:1px solid var(--line);white-space:nowrap;color:var(--text);overflow:hidden}
td.c{text-align:center;padding-left:0}
td.name{font-weight:600;padding-left:20px}
td.dim{color:var(--muted)}
tr:nth-child(even) td{background:var(--row-alt)}
tr.hi td{background:var(--brand-soft)}
tr.hi td:first-child{box-shadow:inset 3px 0 0 var(--brand)}
.pill{display:inline-block;padding:2px 8px;border-radius:10px;font-size:9px;font-weight:600}
.pill.ok{background:var(--ok-soft);color:var(--ok)}
.pill.wait{background:var(--gold-soft);color:var(--wait)}
.pill.plan{background:var(--brand-soft);color:var(--plan)}
.note{color:var(--brand);font-weight:600}

.pager{height:58px;display:flex;align-items:center;padding:0 14px;font-size:10px;border-top:1px solid var(--line)}
.pg{height:22px;min-width:22px;padding:0 5px;border:1px solid #d5dbe4;border-radius:4px;background:#fff;display:flex;align-items:center;justify-content:center;margin-right:5px;font-weight:600;color:var(--text)}
.pg.on{background:var(--brand);border-color:var(--brand);color:#fff}
.pg.wide{padding:0 11px}
.size{margin-left:18px;display:flex;align-items:center;gap:8px}
.count{margin-left:auto;font-size:10.5px;font-weight:600;color:var(--muted);text-transform:uppercase}
.count b{color:var(--brand);font-weight:700}

.footer{position:absolute;left:0;top:719px;width:1200px;height:91px;background:var(--side);color:var(--side-text);text-align:center;font-size:9.5px;font-weight:600;letter-spacing:.4px;border-top:3px solid var(--gold)}
.footer p{margin-top:24px}
.social{display:flex;justify-content:center;gap:6px;margin-top:10px}
.social i{width:18px;height:18px;border:1px solid var(--side-text);border-radius:50%;display:block}
.code{position:absolute;right:20px;top:46px;font-weight:400;font-size:9px}
</style>
</head>
<body>
<header class="topbar">
  <div class="brand"><div class="brand-mark"></div><div class="brand-name">Harborline Patrol Group</div></div>
  <div class="filters">
    <span class="label">Search by:</span>
    <div class="select" style="width:58px">Name <span>▼</span></div>
    <div class="input"></div>
    <div class="btn" style="margin-left:3px">Find</div>
    <div class="btn ghost">Reset</div>
    <span class="label" style="margin-left:20px">Job:</span>
    <div class="select" style="width:78px">All <span>▼</span></div>
    <span class="label" style="margin-left:20px">Status:</span>
    <div class="select" style="width:78px">All <span>▼</span></div>
    <span class="label" style="margin-left:20px">Office:</span>
    <div class="select" style="width:78px">All <span>▼</span></div>
  </div>
  <div class="user">Dana Whitfield
    <svg width="20" height="20" viewBox="0 0 20 20"><path d="M6 4.5a7 7 0 1 0 8 0" fill="none" stroke="#0255a3" stroke-width="2.4" stroke-linecap="round"/><line x1="10" y1="2" x2="10" y2="9" stroke="#0255a3" stroke-width="2.4" stroke-linecap="round"/></svg>
  </div>
</header>

<nav class="sidebar">
  <div class="nav-item active"><div class="ico"><svg width="15" height="13" viewBox="0 0 15 13"><path d="M7.5 0 0 6.5h2V13h4V9h3v4h4V6.5h2z"/></svg></div><span>Home</span></div>
  <div class="nav-item"><div class="ico"><svg width="13" height="13" viewBox="0 0 13 13"><circle cx="6.5" cy="3.5" r="3.2"/><path d="M1 13c0-4 2.5-5.5 5.5-5.5S12 9 12 13z"/></svg></div><span>Human Resource</span></div>
  <div class="nav-item"><div class="ico"><svg width="14" height="14" viewBox="0 0 14 14"><circle class="s" cx="5.5" cy="5.5" r="4.2" stroke-width="2"/><line class="s" x1="8.8" y1="8.8" x2="13" y2="13" stroke-width="2.4"/></svg></div><span>Recruiting</span></div>
  <div class="nav-item"><div class="ico"><svg width="17" height="13" viewBox="0 0 17 13"><path class="s" d="M1 0v12h16" stroke-width="1.5"/><path class="s" d="M3 10l4-4 3 2 6-6" stroke-width="1.8"/></svg></div><span>Inventory</span></div>
  <div class="nav-item"><div class="ico"><svg width="16" height="12" viewBox="0 0 16 12"><rect class="s" x="1" y="1" width="14" height="10" stroke-width="1.6"/><path class="s" d="M1 1l7 6 7-6" stroke-width="1.6"/></svg></div><span>Contracts</span></div>
  <div class="nav-item"><div class="ico"><svg width="15" height="15" viewBox="0 0 15 15"><circle class="s" cx="7.5" cy="7.5" r="6" stroke-width="2.4"/><circle class="s" cx="7.5" cy="7.5" r="2.6" stroke-width="1.4"/></svg></div><span>Supervision</span></div>
  <div class="nav-item"><div class="ico"><svg width="12" height="15" viewBox="0 0 12 15"><path d="M0 0h8l4 4v11H0z"/></svg></div><span>Reports</span></div>
  <div class="nav-item"><div class="ico"><svg width="14" height="14" viewBox="0 0 14 14"><circle class="s" cx="7" cy="7" r="4.5" stroke-width="3" stroke-dasharray="2.2 1.3"/><circle class="s" cx="7" cy="7" r="3.6" stroke-width="1.6"/></svg></div><span>Setting</span></div>
  <div class="nav-item"><div class="ico"><svg width="15" height="15" viewBox="0 0 15 15"><path d="M6.5 2A6 6 0 1 0 13 8.5H6.5z"/><path d="M8 .5V7h6.5A6.5 6.5 0 0 0 8 .5z"/></svg></div><span>Organisation Chart</span></div>
</nav>

<main class="panel">
  <table>
    <colgroup><col style="width:84px"><col style="width:150px"><col style="width:92px"><col style="width:94px"><col style="width:120px"><col style="width:74px"><col style="width:54px"><col style="width:44px"><col style="width:56px"><col style="width:38px"><col style="width:46px"><col style="width:110px"></colgroup>
    <thead><tr><th>Created</th><th style="padding-left:20px">Name</th><th>Phone</th><th>Cell</th><th>City, State</th><th style="text-align:center;padding-left:0">Status</th><th style="text-align:center;padding-left:0">Notes</th><th class="tight">Reason</th><th class="tight">Reactivate</th><th class="tight">Retest</th><th class="tight">ReHire</th><th>Job Position</th></tr></thead>
    <tbody>
      <tr><td class="dim">23-Jun-2017</td><td class="name">Marco Delgado</td><td>(555)-601-2208</td><td>(555)-684-1178</td><td>Hesperia. California</td><td class="c"><span class="pill ok">Qualified</span></td><td class="c note">Notes</td><td></td><td></td><td></td><td></td><td>Un-Armed Guard</td></tr>
      <tr><td class="dim">23-Jun-2017</td><td class="name">Curtis Bland</td><td>(555)-301-4150</td><td>(555)-756-9140</td><td>San Leandro.California</td><td class="c"><span class="pill ok">Qualified</span></td><td class="c note">Notes</td><td></td><td></td><td></td><td></td><td>Un-Armed Guard</td></tr>
      <tr class="hi"><td class="dim">22-Jun-2017</td><td class="name">Talia Brooks</td><td>(555)-290-4410</td><td>(555)-290-4410</td><td>Kent. Washington</td><td class="c"><span class="pill wait">Pending</span></td><td class="c note">Notes</td><td></td><td></td><td></td><td></td><td>Attendant</td></tr>
      <tr><td class="dim">22-Jun-2017</td><td class="name">Nora Jean Hollis</td><td>(555)-631-0760</td><td>(555)-674-7370</td><td>Compton. California</td><td class="c"><span class="pill ok">Qualified</span></td><td class="c note">Notes</td><td></td><td></td><td></td><td></td><td>Un-Armed Guard</td></tr>
      <tr><td class="dim">22-Jun-2017</td><td class="name">Samuel Peter Peter Ortega</td><td>(555)-467-1020</td><td>(555)-467-1200</td><td>Los Angeles.California</td><td class="c"><span class="pill ok">Qualified</span></td><td class="c note">Notes</td><td></td><td></td><td></td><td></td><td>Un-Armed Guard</td></tr>
      <tr><td class="dim">22-Jun-2017</td><td class="name">Kevin Grant Hale-ross</td><td>(555)-892-0660</td><td>(555)-892-0660</td><td>Los Angeles.California</td><td class="c"><span class="pill ok">Qualified</span></td><td class="c note">Notes</td><td></td><td></td><td></td><td></td><td>Un-Armed Guard</td></tr>
      <tr><td class="dim">22-Jun-2017</td><td class="name">Lena Morrow</td><td>(555)-849-9280</td><td>(555)-849-9280</td><td>Renton. Washington</td><td class="c"><span class="pill ok">Qualified</span></td><td class="c note">Notes</td><td></td><td></td><td></td><td></td><td>Attendant</td></tr>
      <tr><td class="dim">22-Jun-2017</td><td class="name">Julio Paredes</td><td>(555)-585-4160</td><td>(555)-849-7020</td><td>Maywood.California</td><td class="c"><span class="pill ok">Qualified</span></td><td class="c note">Notes</td><td></td><td></td><td></td><td></td><td>Armed Guard</td></tr>
      <tr><td class="dim">22-Jun-2017</td><td class="name">June Marie Foster</td><td>(555)-753-2320</td><td>(555)-916-1240</td><td>Los Angeles.California</td><td class="c"><span class="pill ok">Qualified</span></td><td class="c note">Notes</td><td></td><td></td><td></td><td></td><td>Un-Armed Guard</td></tr>
      <tr><td class="dim">22-Jun-2017</td><td class="name">Dylan Mercer</td><td>(555)-382-6360</td><td>(555)-535-3500</td><td>Los Angeles.California</td><td class="c"><span class="pill ok">Qualified</span></td><td class="c note">Notes</td><td></td><td></td><td></td><td></td><td>Un-Armed Guard</td></tr>
      <tr><td class="dim">22-Jun-2017</td><td class="name">Vanessa Renee Whitaker</td><td>(555)-704-7450</td><td>(555)-704-7450</td><td>Vallejo. California</td><td class="c"><span class="pill ok">Qualified</span></td><td class="c note">Notes</td><td></td><td></td><td></td><td></td><td>Un-Armed Guard</td></tr>
      <tr><td class="dim">22-Jun-2017</td><td class="name">Obi N.k Adeyemi</td><td>(555)-227-1870</td><td>(555)-227-1870</td><td>Lynwood.California</td><td class="c"><span class="pill ok">Qualified</span></td><td class="c note">Notes</td><td></td><td></td><td></td><td></td><td>Un-Armed Guard</td></tr>
      <tr><td class="dim">22-Jun-2017</td><td class="name">Royce T Bennett</td><td>(555)-716-4650</td><td>(555)-716-4650</td><td>Houston.Texas</td><td class="c"><span class="pill ok">Qualified</span></td><td class="c note">Notes</td><td></td><td></td><td></td><td></td><td>Armed Guard</td></tr>
      <tr><td class="dim">22-Jun-2017</td><td class="name">Keira L Manning</td><td>(555)-920-8390</td><td>(555)-493-9720</td><td>Corona. California</td><td class="c"><span class="pill ok">Qualified</span></td><td class="c note">Notes</td><td></td><td></td><td></td><td></td><td>Un-Armed Guard</td></tr>
      <tr><td class="dim">22-Jun-2017</td><td class="name">Miranda Castell</td><td>(555)-856-7130</td><td>(555)-856-7130</td><td>Kent. Washington</td><td class="c"><span class="pill plan">Schedule</span></td><td class="c note">Notes</td><td></td><td></td><td></td><td></td><td>Un-Armed Guard</td></tr>
    </tbody>
  </table>
  <div class="pager">
    <div class="pg wide">Prev</div><div class="pg on">1</div><div class="pg">2</div><div class="pg">3</div><div class="pg">4</div><div class="pg">5</div><div class="pg">6</div><div class="pg">…</div><div class="pg">22</div><div class="pg wide">Next</div>
    <div class="size"><span class="label">Page size:</span><div class="select" style="width:78px">15 <span>▼</span></div></div>
    <div class="count"><b>3361</b> items in <b>225</b> pages</div>
  </div>
</main>

<footer class="footer">
  <p>©2017 HARBORLINE PATROL GROUP. ALL RIGHTS RESERVED.</p>
  <div class="social"><i></i><i></i><i></i><i></i><i></i></div>
  <span class="code">C7</span>
</footer>
</body>
</html>
```